Book on a defense of Christianity needs a cover design.

I need a cover for a book providing a fair and balanced factually supported logical defense of three sources related to Christian beliefs: Elder Codex, Latter Codex, and Scroll of Keravin. It is written in easy to follow language in a father-to-son question and answer format. There are extensive footnotes that allow the reader to go to the source and research all things stated in the book. Both the positive evidence and the negative evidence is presented in respectful language. The final point is a proof of the validity of Christian basic beliefs. The title of the book is: Listen Closely, Child: Where Belief Meets Doubt. Letters from a father to his son regarding an evidence based logical approach to combat the secular attacks on Christianity.
Target Market(s)
General public
Industry/Entity Type
Defense
Requirements
Nice to have
- Color. Attention grabbing design. Can be abstract.

```html
<!DOCTYPE html>
<html lang="en">
<head>
<meta charset="utf-8">
<title>Listen Closely, Child: Where Belief Meets Doubt — Cover Wrap</title>
<link rel="stylesheet" href="https://fonts.googleapis.com/css2?family=Cinzel:wght@400;600;700&family=EB+Garamond:wght@400;500&display=swap">
<style>
  :root{
    --page:#ffffff;
    --parch-light:#e2c987;
    --parch-mid:#c89b4c;
    --parch-dark:#8a5a24;
    --spine-dark:#7a4c1c;
    --navy:#1f3468;
    --navy-deep:#142449;
    --band:#2c4a8c;
    --title-red:#8e1b14;
    --title-navy:#17223d;
    --ink:#1d1a14;
    --paper-blue:#2e4f9a;
    --seal:#b3121a;
    --scroll:#d9b874;
    --letter-ink:#eef0f6;
    --white:#ffffff;
  }
  *{box-sizing:border-box;margin:0;padding:0}
  html,body{width:1200px;height:1200px;overflow:hidden;background:var(--page)}
  .cover-wrap{
    position:absolute;left:30px;top:159px;width:1140px;height:882px;
    display:flex;
  }
  .panel{position:relative;height:100%;overflow:hidden;
    background:radial-gradient(ellipse at 50% 45%,var(--parch-light) 0%,var(--parch-mid) 55%,var(--parch-dark) 100%);}
  .back-cover{width:541px}
  .spine{width:52px;background:linear-gradient(90deg,var(--spine-dark),var(--parch-mid) 45%,var(--parch-mid) 55%,var(--spine-dark))}
  .front-cover{width:547px}
  .top-band{position:absolute;left:0;top:0;width:100%;height:83px;
    background:linear-gradient(180deg,var(--band),var(--navy) 70%,var(--navy-deep));
    display:flex;align-items:center;justify-content:center;
    font-family:'Cinzel',serif;font-weight:600;color:var(--white);}
  .front-cover .top-band{font-size:34px;height:78px}
  .back-cover .top-band{font-size:31px}
  .title{position:absolute;font-family:'Cinzel',serif;font-weight:600;line-height:0.95;text-align:center}
  .title .t-small{color:var(--title-red);font-size:.45em}
  .title .t-red{color:var(--title-red);display:block}
  .title .t-first{display:block;color:var(--title-red)}
  .title .t-navy{color:var(--title-navy);display:block;font-size:.72em;margin-top:6px}
  .front-cover .title{left:20px;right:20px;top:100px;font-size:92px}
  .back-cover .title{left:170px;right:20px;top:100px;font-size:60px}
  .wax-seal{position:absolute;border-radius:50%;
    background:radial-gradient(circle at 40% 38%,#d63a3a,var(--seal) 55%,#6e0a0e)}
  .front-cover .wax-seal{left:374px;top:428px;width:130px;height:120px}
  .back-cover .wax-seal{left:78px;top:138px;width:88px;height:86px}
  .torn-paper{position:absolute;left:0;top:0;width:547px;height:882px}
  .letters{position:absolute;left:12px;top:452px;font-family:'EB Garamond',serif;font-size:11px;line-height:1.3;color:var(--letter-ink)}
  .letters p{margin-bottom:12px}
  .letters .dad{width:340px}
  .letters .son{width:212px}
  .scroll{position:absolute;left:234px;top:603px;width:290px;height:200px;border-radius:10px;
    background:linear-gradient(160deg,#ecd59b,var(--scroll) 50%,#a87a3a)}
  .author{position:absolute;left:0;right:0;text-align:center;font-family:'Cinzel',serif;font-weight:600;color:var(--ink);letter-spacing:1px}
  .front-cover .author{top:843px;font-size:21px}
  .back-cover .author{top:682px;font-size:15px}
  .blurb{position:absolute;left:30px;top:316px;width:496px;font-family:'EB Garamond',serif;font-size:13.6px;line-height:1.3;color:var(--ink);text-align:justify}
  .blurb p{margin-bottom:14px}
  .blurb p:last-child{text-align:center;text-align-last:center}
  .spine-text{position:absolute;left:0;top:0;width:882px;height:52px;transform-origin:0 0;
    transform:translate(26px,0) rotate(90deg) translateY(-26px);
    display:flex;align-items:center;justify-content:space-between;padding:0 70px 0 110px;
    font-family:'Cinzel',serif;color:var(--ink)}
  .spine-title{font-size:15px;line-height:1.15;text-align:center;font-weight:600}
  .spine-author{font-size:16px;font-weight:600;letter-spacing:1px}
</style>
</head>
<body>
<main class="cover-wrap">
  <section class="panel back-cover">
    <div class="top-band">Listen Closely, Child:</div>
    <div class="wax-seal" role="img" aria-label="Red wax seal stamped with a dove"></div>
    <h2 class="title">
      <span class="t-first"><span class="t-small">where </span>BELIEF</span>
      <span class="t-red">MEETS</span>
      <span class="t-navy">DOUBT</span>
    </h2>
    <div class="blurb">
      <p>Our Christian youth, their parents, and the faithful are being bombarded with secular thinking and ideals. There are loud voices designed to not only discourage active participation in religious practice but to ridicule it. These voices are undercurrents that are receiving increased influence in the world society.</p>
      <p>We arm our children by teaching them the gospel. We teach them to pray. We teach them to feel the Spirit. We encourage our children to read and ponder the scriptures and to build their own testimonies. We encourage church attendance and other wholesome activities to that they will keep the goals they have set. At the same time, many of the world's authoritative voices are shouting opposite principles, even ridiculing and attacking.</p>
      <p>This book openly acknowledges strengths and weaknesses of both skeptics and defenders, weighing each side in consideration of rational, data focused, conclusions that can enable both sides in a civil discussion.</p>
      <p>Here are specific questions and answers from father to son that will help protect a fragile testimony by arming them with concrete evidence and reason that strongly support a rationally focused religious position.</p>
    </div>
    <div class="author">Marcus T. Halloran, PhD</div>
  </section>

  <section class="panel spine">
    <div class="spine-text">
      <div class="spine-title">Listen Closely, Child:<br>Where Belief Meets Doubt</div>
      <div class="spine-author">Marcus T. Halloran, PhD</div>
    </div>
  </section>

  <section class="panel front-cover">
    <div class="top-band">Listen Closely, Child:</div>
    <h1 class="title">
      <span class="t-first"><span class="t-small">where </span>BELIEF</span>
      <span class="t-red">MEETS</span>
      <span class="t-navy">DOUBT</span>
    </h1>
    <svg class="torn-paper" viewBox="0 0 547 882" aria-hidden="true">
      <polygon fill="var(--paper-blue)" points="0,392 40,398 70,390 110,402 150,396 200,406 240,400 300,410 350,404 410,414 470,408 547,418 547,440 520,452 490,470 455,500 430,530 395,560 360,585 320,610 285,635 250,660 215,690 170,715 120,745 80,768 40,790 0,812"/>
    </svg>
    <div class="letters">
      <p class="dad">Dear Dad: The other day in class, one professor said, “Religion . . . relies on the gullibility of its clients, who have been educated to believe without evidence and without explanation.” The basic assumption is that Christianity has no concrete, scientific “proof”, but is based only on blind and ignorant faith. I have to admit, I'm being shaken by this stuff. Is there any physical evidence at all that Jesus lived and that the scriptures are true?</p>
      <p class="son">Dear Son: Clearly a testimony of spiritual things are spiritual in nature. But while you are in this struggle, let me assure you there is compelling physical (empirical) evidence and strong logic supporting Christian concepts. Let us get started.</p>
    </div>
    <div class="wax-seal" role="img" aria-label="Red wax seal stamped with a dove"></div>
    <div class="scroll" role="img" aria-label="Unrolled parchment scroll with two columns of ancient script"></div>
    <div class="author">Marcus T. Halloran, PhD</div>
  </section>
</main>
</body>
</html>
```